【依頼の目的/概要】
電子書籍(bookrie)の表紙デザインをお願いします。

【画像サイズ】※BRPより抜粋
表紙ファイルの理想的な寸法は2,560×1,600ピクセルです。
注:画像の寸法は10,000×10,000ピクセルです。

【タイトル】
資格試験 ゴールダッシュ・速習・楽々学習術

サブタイトル
通れる学び方

【著者】
行政書士 社会保険労務士
森川澄江

【本の内容】
行政書士試験の勉強を短期間で仕上げて、合格する勉強法を
書いた本です。

【デザイン要望】
特にこだわりません。
素敵なデザインの応募を楽しみにしています。
※次点、次々点の方への参加報酬を設定しました。

その他
必要な情報がありましたらお問い合わせください。

本を以下に添付します。
本文中にエクセルで作成した表を挿入します。

明るく見やすく、わかり易い表現が良かったです。

皆様お疲れ様でした。
T_okabe様には訂正を速攻して頂きありがとうございました。
最後まで迷いました。
皆様のご依頼が増えますことをご祈念申し上げます。

```html
<!DOCTYPE html>
<html lang="ja">
<head>
<meta charset="utf-8">
<title>資格試験 ゴールダッシュ 通れる学び方</title>
<link href="https://fonts.googleapis.com/css2?family=Noto+Sans+JP:wght@500;700;900&family=Pacifico&display=swap" rel="stylesheet">
<style>
  :root {
    --sky: #d9eefa;
    --paper: #ffffff;
    --ink: #161616;
    --blue: #1b8ad6;
    --navy: #1f67b0;
    --red: #e4312b;
    --gold: #f3c43a;
  }
  * { margin: 0; padding: 0; box-sizing: border-box; }
  html, body { width: 750px; height: 1200px; overflow: hidden; background: var(--sky); }
  .cover {
    position: relative; width: 750px; height: 1200px; overflow: hidden;
    background: linear-gradient(180deg, var(--sky) 0%, #eaf6fd 40%, var(--paper) 60%);
    font-family: "Noto Sans JP", sans-serif; color: var(--ink);
  }
  .title-main {
    position: absolute; top: 60px; left: 0; width: 100%; text-align: center;
    font-weight: 900; font-size: 132px; line-height: 1; letter-spacing: 4px;
  }
  .title-dash {
    position: absolute; top: 212px; left: 0; width: 100%; text-align: center;
    font-weight: 900; font-size: 104px; line-height: 1; color: var(--blue);
    -webkit-text-stroke: 3px var(--paper); paint-order: stroke fill;
    text-shadow: 0 0 0 var(--paper);
  }
  .subtitle {
    position: absolute; top: 350px; left: 165px; text-align: center;
    font-weight: 900; font-size: 74px; line-height: 1.12; color: var(--red);
    -webkit-text-stroke: 6px var(--paper); paint-order: stroke fill;
  }
  .tag-speed {
    position: absolute; top: 368px; left: 450px; width: 160px; height: 62px;
    background: var(--blue); color: var(--paper); font-weight: 900; font-size: 40px;
    display: flex; align-items: center; padding-left: 16px; border-radius: 4px;
  }
  .tag-speed svg { position: absolute; right: -30px; top: -8px; }
  .tag-easy {
    position: absolute; top: 448px; left: 450px; width: 160px; height: 88px;
    background: var(--paper); border: 4px solid var(--blue); color: var(--navy);
    font-weight: 900; font-size: 32px; line-height: 1.15; text-align: center;
    display: flex; align-items: center; justify-content: center;
  }
  .hero-art {
    position: absolute; top: 420px; left: 20px; width: 460px; height: 620px;
    border-radius: 46% 46% 30% 30%;
    background: radial-gradient(ellipse at 50% 45%, #f5d9b8 0%, #c8e3f5 45%, rgba(217,238,250,0) 75%);
  }
  .study-art {
    position: absolute; top: 570px; left: 460px; width: 260px; height: 160px;
    border-radius: 20px;
    background: linear-gradient(135deg, #ffffff 0%, #cfe6f6 60%, #f7e3a8 100%);
  }
  .author {
    position: absolute; top: 905px; left: 400px; font-weight: 700;
  }
  .author-role { font-size: 26px; letter-spacing: 2px; }
  .author-name { font-size: 34px; letter-spacing: 6px; margin-top: 4px; }
  .author-name small { font-size: 24px; margin-left: 6px; }
  .band {
    position: absolute; left: 0; bottom: 0; width: 100%; height: 172px;
    background: var(--navy);
  }
  .band-badge {
    position: absolute; left: 16px; top: -22px; width: 150px; height: 110px;
    background: var(--paper); border-radius: 50%;
    transform: rotate(-14deg); display: flex; align-items: center; justify-content: center;
    font-family: "Pacifico", cursive; color: var(--navy); font-size: 30px;
  }
  .band-copy {
    position: absolute; left: 190px; top: 26px; color: var(--paper);
    font-weight: 900; font-size: 50px; line-height: 1.22; text-align: center;
  }
</style>
</head>
<body>
  <main class="cover">
    <h1 class="title-main">資格試験</h1>
    <p class="title-dash">ゴールダッシュ</p>
    <div class="hero-art" role="img" aria-label="両手を上げて喜び跳ぶスーツ姿の男性のイラスト"></div>
    <p class="subtitle">通れる<br>学び方</p>
    <div class="tag-speed">速習
      <svg width="58" height="64" viewBox="0 0 58 64" aria-hidden="true">
        <rect x="22" y="2" width="14" height="7" fill="#161616"/>
        <circle cx="29" cy="36" r="24" fill="#fff" stroke="#161616" stroke-width="4"/>
        <circle cx="29" cy="36" r="18" fill="#f3c43a"/>
        <path d="M29 36 V22 M29 36 L39 40" stroke="#161616" stroke-width="4" stroke-linecap="round"/>
      </svg>
    </div>
    <div class="tag-easy">楽々<br>学習術</div>
    <div class="study-art" role="img" aria-label="開いた本とペンのイラスト"></div>
    <div class="author">
      <p class="author-role">行政書士　社会保険労務士</p>
      <p class="author-name">森川 澄江<small>著</small></p>
    </div>
    <footer class="band">
      <div class="band-badge">Goal Dash!</div>
      <p class="band-copy">行政書士試験を<br>短期間で合格を目指す!</p>
    </footer>
  </main>
</body>
</html>
```